Electrical company needs a brochure designed for electrical construction work

we need a brochure designed for our company BRONZEWAY ELECTRICAL INSTALLATIONS. we are a group of electricians working in the construction industry delivering electrical constructon services to builders and other clients in the commercial and Industrial working environments. we would like our logo to stand out with a dark theme and also give a professional fee.l we have a brief description of what we do and our experiences in a word doc i will provide it along with our logo design

Target Market(s)

builders for commercial and industrial construction projects

Industry/Entity Type

Electric Company

Font styles to use
Serif

Colors
0456a4
96b7d9
5c5c5c
757575
000000
aaaaaa
ec1f27
33a6d7
0493ce

Requirements
Must have
• a professional feel,
Nice to have
• some wording that makes us stand out and brings all the attention

```html
<!DOCTYPE html>
<html lang="en">
<head>
<meta charset="utf-8">
<title>Bronzeway Electrical Installations – Brochure</title>
<link rel="stylesheet" href="https://fonts.googleapis.com/css2?family=Montserrat:wght@600;700;800&family=Open+Sans:wght@400;600;700&display=swap">
<style>
:root{
  --navy:#0456a4; --sky:#96b7d9; --grey-dark:#5c5c5c; --grey:#757575; --black:#000000;
  --grey-light:#aaaaaa; --red:#ec1f27; --cyan:#33a6d7; --blue:#0493ce;
  --charcoal:#2a2b2f; --paper:#ffffff; --stage:#e4e4e4;
}
*{box-sizing:border-box;margin:0;padding:0}
html,body{width:800px;height:1200px;overflow:hidden;background:var(--stage)}
body{font-family:"Open Sans",Arial,sans-serif;color:var(--grey-dark);position:relative}
.spread{position:absolute;left:20px;width:760px;height:537px;display:flex;box-shadow:0 4px 14px rgba(0,0,0,.18)}
.spread--outer{top:30px}
.spread--inner{top:633px}
.page{position:relative;width:380px;height:537px;background:var(--paper);overflow:hidden}
.page svg.deco{position:absolute;inset:0;width:100%;height:100%}
.photo{position:absolute}
.body-copy{position:absolute;font-size:7.2px;line-height:1.5;color:var(--grey-dark);text-align:justify}
.body-copy p+p{margin-top:7px}

/* back page */
.back__copy{left:24px;top:56px;width:186px}
.back__photo-worker{left:22px;top:200px;width:92px;height:120px;background:linear-gradient(160deg,#d9d3c8,#b46a3c 55%,#6d5a4c)}
.back__photo-panel{left:118px;top:200px;width:92px;height:120px;background:linear-gradient(150deg,#c9ccd0,#4b5157 60%,#c7a93a)}
.back__photo-meter{left:222px;top:70px;width:158px;height:270px;background:linear-gradient(170deg,#e6e6e6,#9a9a9a 40%,#d9702a 65%,#3a3a3a)}
.contact{position:absolute;left:24px;top:372px}
.contact__title{font-family:"Montserrat",sans-serif;font-weight:700;font-size:11px;color:var(--red);margin-bottom:8px}
.contact__row{display:flex;align-items:flex-start;gap:7px;font-size:8.5px;color:var(--grey-dark);margin-bottom:5px;line-height:1.3}
.contact__row svg{flex:none;width:9px;height:9px;margin-top:1px}
.brand-mark{position:absolute;display:flex;align-items:center;gap:5px;font-family:"Montserrat",sans-serif;font-weight:800;color:var(--navy);white-space:nowrap}
.brand-mark__dot{border-radius:50%;background:var(--cyan)}
.back__brand{left:228px;top:380px;font-size:10.5px}
.back__brand .brand-mark__dot{width:10px;height:10px}
.socials{position:absolute;left:292px;top:425px;display:flex;gap:6px}
.socials span{width:11px;height:11px;border-radius:50%;background:var(--paper)}
.back__web{position:absolute;left:30px;top:512px;font-size:9.5px;font-weight:600;color:var(--paper);display:flex;gap:7px;align-items:center}

/* front page */
.front{background:var(--charcoal)}
.front__brand{left:70px;top:22px;font-size:17px;color:var(--cyan)}
.front__brand .brand-mark__dot{width:16px;height:16px;background:var(--red)}
.front__photo{left:0;top:66px;width:380px;height:270px;background:linear-gradient(160deg,#f0efe9,#c9c9c6 35%,#8d8f92 60%,#e3c23a 85%,#7a7c80)}
.front__headline{position:absolute;right:26px;top:382px;text-align:right}
.front__headline h1{font-family:"Montserrat",sans-serif;font-weight:800;font-size:25px;color:var(--cyan);letter-spacing:.5px}
.front__headline p{font-size:11px;color:var(--paper);margin-top:3px}
.front__call{position:absolute;left:26px;top:500px;font-family:"Montserrat",sans-serif;font-weight:700;font-size:10.5px;color:var(--paper);letter-spacing:.4px}
.front__abn{position:absolute;right:16px;top:462px;font-family:"Montserrat",sans-serif;font-weight:700;font-size:9px;color:var(--paper)}

/* inner left */
.inner-left__photo{left:0;top:0;width:380px;height:240px;background:linear-gradient(170deg,#b5b8bb,#ece8df 35%,#d8d3c7 65%,#7b7e83)}
.intro{position:absolute;left:30px;top:238px;width:320px;font-size:7.4px;line-height:1.5;color:var(--paper);text-align:justify}
.projects{position:absolute;left:34px;top:346px;list-style:none}
.projects li{display:flex;gap:6px;align-items:center;font-size:7.6px;font-weight:700;color:#222;line-height:1.4}
.projects svg{flex:none;width:8px;height:8px}

/* inner right */
.inner-right__copy{left:26px;top:34px;width:330px}
.inner-right__photo{left:0;top:212px;width:380px;height:300px;background:linear-gradient(160deg,#c6c9cd,#6c7178 40%,#e7b21f 60%,#3f6fb0 85%,#2c2f34)}
</style>
</head>
<body>

<!-- Outer spread: back cover + front cover -->
<section class="spread spread--outer">
  <article class="page back">
    <svg class="deco" viewBox="0 0 380 537" aria-hidden="true">
      <polygon points="0,30 190,0 206,0 0,36" fill="var(--red)"/>
      <polygon points="206,0 380,0 380,4 212,4" fill="var(--cyan)"/>
      <path d="M120 537 C 180 420, 300 380, 380 360 L380 372 C 300 395, 200 440, 150 537 Z" fill="var(--sky)" opacity=".25"/>
      <polygon points="200,470 380,400 380,450 240,487" fill="var(--blue)"/>
      <polygon points="0,500 230,500 260,487 380,450 380,537 0,537" fill="var(--red)"/>
    </svg>
    <div class="body-copy back__copy">
      <p>Electrical contracting company able to perform a great variety of electrical work, with experience on heavy industrial installs and commercial fit outs. We have taken part in many large construction jobs around Darwin.</p>
      <p>We are a small company just getting started, working part time for over a year on late nights and weekends. We are building our company to work full time and grow into something we can be proud of.</p>
    </div>
    <div class="photo back__photo-worker" role="img" aria-label="Electrician in hard hat checking a switchboard"></div>
    <div class="photo back__photo-panel" role="img" aria-label="Open switchboard with cabling"></div>
    <div class="photo back__photo-meter" role="img" aria-label="Gloved hand holding a digital multimeter"></div>

    <div class="contact">
      <h2 class="contact__title">CONTACT DETAILS</h2>
      <div class="contact__row">
        <svg viewBox="0 0 10 10"><path d="M5 0.5a3 3 0 0 1 3 3c0 2.4-3 6-3 6s-3-3.6-3-6a3 3 0 0 1 3-3z" fill="var(--red)"/><circle cx="5" cy="3.5" r="1.1" fill="#fff"/></svg>
        <span>Address line 1<br>Address line 2, Address line 2</span>
      </div>
      <div class="contact__row">
        <svg viewBox="0 0 10 10"><path d="M2 1l2 .4.6 2-1.2 1a6 6 0 0 0 2.2 2.2l1-1.2 2 .6.4 2c-4 .6-8-3.4-7-7z" fill="var(--red)"/></svg>
        <span>0400 555 218</span>
      </div>
      <div class="contact__row">
        <svg viewBox="0 0 10 10"><rect x="0.5" y="2" width="9" height="6.5" fill="none" stroke="var(--red)" stroke-width="1"/><path d="M0.5 2.2 5 5.6 9.5 2.2" fill="none" stroke="var(--red)" stroke-width="1"/></svg>
        <span>office@bronzewaymail.com.au</span>
      </div>
    </div>

    <div class="brand-mark back__brand"><span class="brand-mark__dot"></span>BRONZEWAY</div>
    <div class="socials" aria-label="Social links"><span></span><span></span><span></span></div>
    <div class="back__web">
      <svg width="10" height="10" viewBox="0 0 10 10"><circle cx="5" cy="5" r="4.3" fill="none" stroke="#fff"/><path d="M.7 5h8.6M5 .7c-2.4 2.6-2.4 6 0 8.6M5 .7c2.4 2.6 2.4 6 0 8.6" fill="none" stroke="#fff" stroke-width=".8"/></svg>
      www.bronzewayelectrical.com.au
    </div>
  </article>

  <article class="page front">
    <div class="brand-mark front__brand"><span class="brand-mark__dot"></span>BRONZEWAY</div>
    <div class="photo front__photo" role="img" aria-label="Gloved hand testing circuit breakers in a switchboard"></div>
    <svg class="deco" viewBox="0 0 380 537" aria-hidden="true">
      <polygon points="0,336 380,336 380,318 0,346" fill="var(--charcoal)"/>
      <polygon points="120,350 380,322 380,330 140,352" fill="var(--red)"/>
      <polygon points="0,487 250,487 280,480 380,452 380,537 0,537" fill="var(--blue)"/>
      <polygon points="230,475 380,436 380,478 250,487" fill="var(--red)"/>
    </svg>
    <div class="front__headline">
      <h1>WE ARE THE BEST</h1>
      <p>Electrical contracting company near you</p>
    </div>
    <div class="front__abn">ABN: 00 0000 000 00</div>
    <div class="front__call">CALL NOW - 0400 555 218</div>
  </article>
</section>

<!-- Inner spread -->
<section class="spread spread--inner">
  <article class="page inner-left">
    <div class="photo inner-left__photo" role="img" aria-label="Rows of wired terminal blocks on a DIN rail"></div>
    <svg class="deco" viewBox="0 0 380 537" aria-hidden="true">
      <polygon points="0,240 380,216 380,300 0,340" fill="var(--red)"/>
      <path d="M0 470 C 60 420, 130 400, 180 410" fill="none" stroke="var(--sky)" stroke-width="10" opacity=".25"/>
      <polygon points="0,520 380,530 380,533 0,523" fill="var(--red)"/>
      <polygon points="0,526 380,534 380,537 0,529" fill="var(--cyan)"/>
    </svg>
    <p class="intro">I'm Dean Whitcombe, a local electrician in Darwin running a small electrical contracting company, Bronzeway Electrical Installations. If you are in need of reliable, punctual and experienced electricians to work on your project, please give me a call. I'm happy to discuss any business or submit a quote for any work you may have. I have worked on a lot of commercial and industrial construction jobs around Darwin for at least the last 10 years. Some jobs include:</p>
    <ul class="projects">
      <li><svg viewBox="0 0 8 8"><path d="M1 4.2 3 6.2 7 1.8" fill="none" stroke="var(--cyan)" stroke-width="1.4"/></svg>Northgate high school</li>
      <li><svg viewBox="0 0 8 8"><path d="M1 4.2 3 6.2 7 1.8" fill="none" stroke="var(--cyan)" stroke-width="1.4"/></svg>St Brigid's catholic college</li>
      <li><svg viewBox="0 0 8 8"><path d="M1 4.2 3 6.2 7 1.8" fill="none" stroke="var(--cyan)" stroke-width="1.4"/></svg>Underground cabling on many subdivisions including Eastbrook, Hillcrest, Ridgeview</li>
      <li><svg viewBox="0 0 8 8"><path d="M1 4.2 3 6.2 7 1.8" fill="none" stroke="var(--cyan)" stroke-width="1.4"/></svg>Central office fit outs</li>
      <li><svg viewBox="0 0 8 8"><path d="M1 4.2 3 6.2 7 1.8" fill="none" stroke="var(--cyan)" stroke-width="1.4"/></svg>Harbourside substation HV switch gear</li>
      <li><svg viewBox="0 0 8 8"><path d="M1 4.2 3 6.2 7 1.8" fill="none" stroke="var(--cyan)" stroke-width="1.4"/></svg>The waterfront HV switch gear</li>
      <li><svg viewBox="0 0 8 8"><path d="M1 4.2 3 6.2 7 1.8" fill="none" stroke="var(--cyan)" stroke-width="1.4"/></svg>Bayline receiving station wave pool etc</li>
      <li><svg viewBox="0 0 8 8"><path d="M1 4.2 3 6.2 7 1.8" fill="none" stroke="var(--cyan)" stroke-width="1.4"/></svg>Northern barracks single leap project</li>
      <li><svg viewBox="0 0 8 8"><path d="M1 4.2 3 6.2 7 1.8" fill="none" stroke="var(--cyan)" stroke-width="1.4"/></svg>Parliament house multiple contracts</li>
      <li><svg viewBox="0 0 8 8"><path d="M1 4.2 3 6.2 7 1.8" fill="none" stroke="var(--cyan)" stroke-width="1.4"/></svg>The convention centre</li>
      <li><svg viewBox="0 0 8 8"><path d="M1 4.2 3 6.2 7 1.8" fill="none" stroke="var(--cyan)" stroke-width="1.4"/></svg>Airbase runway lighting</li>
      <li><svg viewBox="0 0 8 8"><path d="M1 4.2 3 6.2 7 1.8" fill="none" stroke="var(--cyan)" stroke-width="1.4"/></svg>Airport multiple different contracts</li>
      <li><svg viewBox="0 0 8 8"><path d="M1 4.2 3 6.2 7 1.8" fill="none" stroke="var(--cyan)" stroke-width="1.4"/></svg>Hospital oncology building</li>
      <li><svg viewBox="0 0 8 8"><path d="M1 4.2 3 6.2 7 1.8" fill="none" stroke="var(--cyan)" stroke-width="1.4"/></svg>Hospital multiple various maintenance contracts</li>
      <li><svg viewBox="0 0 8 8"><path d="M1 4.2 3 6.2 7 1.8" fill="none" stroke="var(--cyan)" stroke-width="1.4"/></svg>Regional correctional facility</li>
    </ul>
  </article>

  <article class="page inner-right">
    <svg class="deco" viewBox="0 0 380 537" aria-hidden="true">
      <path d="M260 0 C 330 60, 360 120, 380 180" fill="none" stroke="var(--sky)" stroke-width="12" opacity=".25"/>
    </svg>
    <div class="body-copy inner-right__copy">
      <p>This list is not every job I have worked on but it gives a clear picture of what work I can perform as an electrical contractor. Most of the listed jobs I worked on in a leading role, supervising crews and working with other contractors to achieve the best possible result, and I pride myself on my quality of work, work ethics and reliability.</p>
      <p>Recently the opportunity arose that we could move away from our employers and take the business to a new level and work full time with 100% commitment. We believe that our drive and passion for the trade and industry will set us apart and help us exceed any expectations that are placed upon us.</p>
      <p>Our background in large commercial and industrial construction jobs around Darwin has granted us the ability to introduce and implement strong safety practices, so everyone on site goes home safe at the end of every day.</p>
    </div>
    <div class="photo inner-right__photo" role="img" aria-label="Hands holding multimeter probes at a switchboard"></div>
    <svg class="deco" viewBox="0 0 380 537" aria-hidden="true">
      <polygon points="0,512 380,512 380,524 0,524" fill="var(--cyan)"/>
      <polygon points="0,524 380,524 380,537 0,537" fill="var(--red)"/>
    </svg>
  </article>
</section>

</body>
</html>
```